Project: PLWT Biz Cards
PLWT Biz Cards - Construction
Professional
Derek M. Hollis
not using an address on biz cards
derek.hollis@pave-ro.com
www.patiotilesmadebest.com
We are interested in biz card and all stationary items!! Our logo is attached. If you chose not to use our logo, definitely incorporate the logo's look and feel. Use icons to stipulate phone, fax, website, etc rather than words.
Use logo or other design.
Garage Garage
we are running out of time. 6 minutes Did you get my other emails? Just fretting a bit. :-)

```html
<!DOCTYPE html>
<html lang="en">
<head>
<meta charset="utf-8">
<title>PLWT Business Cards</title>
<link href="https://fonts.googleapis.com/css2?family=Open+Sans:wght@400;600;800&display=swap" rel="stylesheet">
<style>
  :root {
    --bg: #1c1c1c;
    --card: #ffffff;
    --ink: #222222;
    --muted: #6b6b6b;
    --red: #d3222a;
    --band: #141414;
    --band-text: #f2f2f2;
  }
  * { margin: 0; padding: 0; box-sizing: border-box; }
  html, body { width: 1200px; height: 802px; overflow: hidden; }
  body {
    background: var(--bg);
    font-family: "Open Sans", Arial, sans-serif;
    position: relative;
  }
  .card {
    position: absolute;
    width: 540px;
    height: 310px;
    background: var(--card);
    overflow: hidden;
    box-shadow: 0 10px 30px rgba(0,0,0,.5);
  }
  .card--front { left: 40px; top: 246px; }
  .card--back  { left: 620px; top: 246px; }

  .card__band { position: absolute; left: 0; bottom: 0; width: 540px; height: 110px; }
  .card__web {
    position: absolute; left: 0; right: 0; bottom: 18px;
    text-align: center; color: var(--band-text);
    font-size: 13px; font-weight: 600; letter-spacing: .5px;
  }

  .logo { display: flex; align-items: center; gap: 10px; }
  .logo__mark { width: 14px; height: 14px; background: var(--red); }
  .logo__name { font-weight: 800; color: var(--ink); letter-spacing: 2px; }

  .card--front .logo { position: absolute; left: 30px; top: 26px; }
  .card--front .logo__name { font-size: 38px; }

  .contacts { position: absolute; left: 32px; top: 104px; list-style: none; }
  .contacts li {
    display: flex; align-items: center; gap: 8px;
    font-size: 10.5px; color: var(--muted); height: 21px;
  }
  .contacts svg { width: 12px; height: 12px; fill: var(--red); flex: none; }

  .person { position: absolute; left: 300px; top: 112px; }
  .person__name { color: var(--red); font-size: 14px; font-weight: 600; text-transform: uppercase; letter-spacing: .5px; }
  .person__title { color: var(--muted); font-size: 10.5px; margin-top: 2px; }

  .card--back .logo { position: absolute; left: 0; right: 0; top: 82px; justify-content: center; }
  .card--back .logo__name { font-size: 56px; }
</style>
</head>
<body>

<section class="card card--front" aria-label="Business card front">
  <div class="logo">
    <span class="logo__mark"></span>
    <span class="logo__name">PLWT</span>
  </div>

  <ul class="contacts">
    <li><svg viewBox="0 0 12 12"><path d="M2.4 1l2 2.2-1 1.3c.7 1.5 1.8 2.6 3.2 3.2l1.3-1 2.1 2-1.2 1.8C5.3 10.3 1.6 6.6 1 2.2z"/></svg>410 555 0182</li>
    <li><svg viewBox="0 0 12 12"><rect x="3" y="1" width="6" height="3"/><rect x="1" y="4.5" width="10" height="4.5" rx="1"/><rect x="3" y="8" width="6" height="3"/></svg>410 555 0183</li>
    <li><svg viewBox="0 0 12 12"><rect x="3" y="0.5" width="6" height="11" rx="1"/></svg>410 555 0196</li>
    <li><svg viewBox="0 0 12 12"><path d="M0.5 2h11v8h-11z M1.3 2.6L6 6.6l4.7-4z" fill-rule="evenodd"/></svg>derek.hollis@pave-ro.com</li>
    <li><svg viewBox="0 0 12 12"><circle cx="6" cy="6" r="5.5"/></svg>www.patiotilesmadebest.com</li>
  </ul>

  <div class="person">
    <p class="person__name">Derek M. Hollis</p>
    <p class="person__title">Managing Director</p>
  </div>

  <svg class="card__band" viewBox="0 0 540 110" preserveAspectRatio="none" aria-hidden="true">
    <path d="M0 18 C150 40 330 52 540 34 L540 46 C330 66 150 56 0 34 Z" fill="var(--red)"/>
    <path d="M0 40 C150 62 330 70 540 52 L540 110 L0 110 Z" fill="var(--band)"/>
  </svg>
  <p class="card__web">www.patiotilesmadebest.com</p>
</section>

<section class="card card--back" aria-label="Business card back">
  <div class="logo">
    <span class="logo__mark"></span>
    <span class="logo__name">PLWT</span>
  </div>

  <svg class="card__band" viewBox="0 0 540 110" preserveAspectRatio="none" aria-hidden="true">
    <path d="M0 30 C180 52 360 54 540 22 L540 34 C360 68 180 66 0 44 Z" fill="var(--red)"/>
    <path d="M0 52 C180 74 360 74 540 42 L540 110 L0 110 Z" fill="var(--band)"/>
  </svg>
  <p class="card__web">www.patiotilesmadebest.com</p>
</section>

</body>
</html>
```